Plumbing company needs Business Card Design

Hi I need business card design based on logo which I uploaded. Its plumbing and heating company called Kranex Usługi Hydrauliczno-Gazowe. I want to see on my card motto of my company which is "...od naprawy kranu po remont całej łazienki.", my phone number, name, and website: 617248390, Marek Kowalczyk, info@kranex.org, www.kranex.org
I want to see logos of companys which I'm approved installer (Termolux) (La Valmont) (Corvo) (Pluma).
I want new creative look of business card. I like rounded corners.
Any questions please send message.
Thanks for intrest.
Business
Contact Information for Business Card
Marek Kowalczyk
617 248 390
info@kranex.org
www.kranex.org
...od naprawy kranu po remont całej łazienki.

```html
<!DOCTYPE html>
<html lang="pl">
<head>
<meta charset="utf-8">
<title>Kranex – wizytówki</title>
<link href="https://fonts.googleapis.com/css2?family=Roboto:wght@400;700;900&family=Roboto+Condensed:wght@700&display=swap" rel="stylesheet">
<style>
  :root{
    --bg:#1d1d1f;
    --paper:#f3f3f3;
    --navy:#0f2a6b;
    --red:#d40f14;
    --white:#ffffff;
    --ink:#222222;
  }
  html,body{margin:0;padding:0;width:1200px;height:1000px;overflow:hidden;background:var(--bg);}
  .canvas{position:relative;width:1200px;height:1000px;font-family:"Roboto",Arial,sans-serif;}
  .card{position:absolute;width:407px;height:257px;border-radius:12px;overflow:hidden;background:var(--paper);}
  .card--front{left:173px;top:253px;}
  .card--alt{left:627px;top:253px;}
  .card--back{left:402px;top:556px;background:var(--navy);}

  .brand{position:absolute;left:30px;top:30px;color:var(--red);font-family:"Roboto Condensed",Arial,sans-serif;font-weight:700;line-height:1;}
  .brand__name{font-size:44px;display:block;}
  .brand__tag{font-size:14px;display:block;margin-top:6px;}

  .mascot{position:absolute;left:222px;top:38px;width:160px;height:170px;border-radius:50% 50% 16px 16px;
    background:radial-gradient(circle at 50% 45%, rgba(180,180,180,.45), rgba(200,200,200,.15) 70%);}
  .card--back .mascot{background:radial-gradient(circle at 50% 45%, rgba(255,255,255,.12), rgba(255,255,255,.03) 70%);}

  .person{position:absolute;left:28px;color:var(--navy);font-weight:700;letter-spacing:.3px;margin:0;}
  .card--front .person{top:143px;font-size:18px;}
  .card--alt .person{top:147px;font-size:16px;}

  .icon{display:inline-flex;width:13px;height:13px;border-radius:2px;background:var(--red);align-items:center;justify-content:center;flex:none;}
  .icon svg{width:9px;height:9px;}

  .contact-bar{position:absolute;left:0;bottom:0;width:100%;height:54px;background:var(--navy);border-top:4px solid var(--red);
    display:flex;align-items:center;gap:16px;padding-left:30px;box-sizing:border-box;}
  .contact{display:flex;align-items:center;gap:6px;color:var(--white);font-size:13px;}

  .contact-list{position:absolute;left:28px;top:180px;margin:0;padding:0;list-style:none;}
  .contact-list li{display:flex;align-items:center;gap:8px;color:var(--ink);font-size:12px;height:17px;}

  .motto{position:absolute;left:166px;top:207px;width:222px;height:22px;border-radius:11px;background:var(--navy);
    border:1px solid #8fa0c8;box-sizing:border-box;color:var(--white);font-size:9.5px;font-weight:700;
    display:flex;align-items:center;justify-content:center;white-space:nowrap;}

  .phone-big{position:absolute;left:28px;top:120px;display:flex;align-items:center;gap:9px;color:var(--white);font-size:20px;}
  .phone-big .icon{width:16px;height:16px;}
  .phone-big .icon svg{width:11px;height:11px;}

  .partners{position:absolute;left:0;top:166px;width:100%;height:63px;background:var(--paper);
    display:flex;align-items:center;justify-content:space-around;padding:0 14px;box-sizing:border-box;}
  .partner{color:var(--navy);font-weight:900;font-size:17px;}
  .back-band{position:absolute;left:0;bottom:0;width:100%;height:28px;background:var(--red);}
</style>
</head>
<body>
<div class="canvas">

  <section class="card card--front">
    <div class="mascot" role="img" aria-label="Faint plumber mascot illustration"></div>
    <div class="brand"><span class="brand__name">Kranex</span><span class="brand__tag">Usługi Hydrauliczno-Gazowe</span></div>
    <p class="person">MAREK KOWALCZYK</p>
    <div class="contact-bar">
      <span class="contact"><span class="icon"><svg viewBox="0 0 10 10"><path d="M2 1l2 2-1 1c.6 1.2 1.6 2.2 3 3l1-1 2 2-1.5 1.5C4.5 9 1 5.5.5 2.5z" fill="#fff"/></svg></span>617 248 390</span>
      <span class="contact"><span class="icon"><svg viewBox="0 0 10 10"><rect x="1" y="2" width="8" height="6" fill="none" stroke="#fff"/><path d="M1 2l4 3 4-3" fill="none" stroke="#fff"/></svg></span>info@kranex.org</span>
      <span class="contact"><span class="icon"><svg viewBox="0 0 10 10"><circle cx="5" cy="5" r="4" fill="none" stroke="#fff"/><path d="M1 5h8M5 1c-2 2.5-2 5.5 0 8M5 1c2 2.5 2 5.5 0 8" fill="none" stroke="#fff" stroke-width=".8"/></svg></span>www.kranex.org</span>
    </div>
  </section>

  <section class="card card--alt">
    <div class="mascot" role="img" aria-label="Faint plumber mascot illustration"></div>
    <div class="brand"><span class="brand__name">Kranex</span><span class="brand__tag">Usługi Hydrauliczno-Gazowe</span></div>
    <p class="person">MAREK KOWALCZYK</p>
    <ul class="contact-list">
      <li><span class="icon"><svg viewBox="0 0 10 10"><path d="M2 1l2 2-1 1c.6 1.2 1.6 2.2 3 3l1-1 2 2-1.5 1.5C4.5 9 1 5.5.5 2.5z" fill="#fff"/></svg></span>617 248 390</li>
      <li><span class="icon"><svg viewBox="0 0 10 10"><rect x="1" y="2" width="8" height="6" fill="none" stroke="#fff"/><path d="M1 2l4 3 4-3" fill="none" stroke="#fff"/></svg></span>info@kranex.org</li>
      <li><span class="icon"><svg viewBox="0 0 10 10"><circle cx="5" cy="5" r="4" fill="none" stroke="#fff"/><path d="M1 5h8M5 1c-2 2.5-2 5.5 0 8M5 1c2 2.5 2 5.5 0 8" fill="none" stroke="#fff" stroke-width=".8"/></svg></span>www.kranex.org</li>
    </ul>
    <div class="motto">...od naprawy kranu po remont całej łazienki</div>
  </section>

  <section class="card card--back">
    <div class="mascot" role="img" aria-label="Faint plumber mascot illustration"></div>
    <div class="brand"><span class="brand__name">Kranex</span><span class="brand__tag">Usługi Hydrauliczno-Gazowe</span></div>
    <div class="phone-big"><span class="icon"><svg viewBox="0 0 10 10"><path d="M2 1l2 2-1 1c.6 1.2 1.6 2.2 3 3l1-1 2 2-1.5 1.5C4.5 9 1 5.5.5 2.5z" fill="#fff"/></svg></span>617 248 390</div>
    <div class="partners">
      <span class="partner">Termolux</span>
      <span class="partner">Corvo</span>
      <span class="partner">La Valmont</span>
      <span class="partner">Pluma</span>
    </div>
    <div class="back-band"></div>
  </section>

</div>
</body>
</html>
```